Business card and stationery design

Harbourlight Gatherings Co. is a leading event and conference design and management company.
Please view lumorahostgroup.com.au

The business cards needs to convey:
- professionalism and competency
- exclusivity
- memorable experiences and quality

The business card needs to have the following aspects:
- double sided
- Full colour CMYK
- Printed on either high gloss matt card (designer to recommend)

For the business stationery we require:
- Letterhead with top banner and bottom footer
- A thank you card design
- a with compliments slip design
- a MS powerpoint and MS publisher client presentation slide design which includes cover page and then a standard presentation page
(Note- we do NOT require an envelope design- who sends letters these days!)

The company image is using the key colours of gold, silver and black.
A black background to the business card has been used before and is preferred although we are open to options.

Target Market(s)

High end corporations and businesses that require their events and conferences to be exceptionally well designed and managed

Industry/Entity Type

Business

Contact Information for Business Card

FRONT:

Darian Whitlock
- Event and Conference Specialist

Mobile- +61 (0) 491 238 604
Office- 1300 617 482
dariannw@lumorahostgroup.com.au

Web- lumorahostgroup.com.au

BACK:

- Event and

Font styles to use
Other font styles liked:
• The logo designer used Trajan Pro Bold 3 for the font text in the logo

Requirements
Must have
• Amazing design of the following:
• - business card (double sided)
• - letterhead
• - client thank you card
• - powerpoint and publisher client presentation design files

```html
<!DOCTYPE html>
<html lang="en">
<head>
<meta charset="utf-8">
<title>Harbourlight Gatherings Co. — Business Card</title>
<link rel="stylesheet" href="https://fonts.googleapis.com/css2?family=Cinzel:wght@600&family=Roboto+Condensed:wght@400;700&display=swap">
<style>
  :root {
    --stage-top: #e4e3e6;
    --stage-bottom: #bdbcc0;
    --card: #2c2c2c;
    --gold: #d4ad45;
    --gold-light: #f0d47c;
    --gold-deep: #a9832a;
    --silver: #d9d9d9;
    --text-light: #e6e6e6;
    --text-muted: #cfcfcf;
  }
  * { margin: 0; padding: 0; box-sizing: border-box; }
  html, body { width: 1200px; height: 887px; overflow: hidden; }
  body {
    background: radial-gradient(ellipse at 50% 10%, var(--stage-top) 0%, var(--stage-bottom) 100%);
    font-family: "Roboto Condensed", Arial, sans-serif;
    position: relative;
  }
  .card {
    position: absolute;
    top: 298px;
    width: 520px;
    height: 290px;
    background: var(--card);
    border-radius: 16px;
    overflow: hidden;
    box-shadow: 0 4px 10px rgba(0,0,0,0.28);
  }
  .card--front { left: 50px; }
  .card--back { left: 630px; }

  .brand {
    position: absolute;
    display: flex;
    flex-direction: column;
    align-items: center;
  }
  .brand__dot {
    border-radius: 50%;
    background: var(--gold);
  }
  .brand__name {
    font-family: "Cinzel", "Times New Roman", serif;
    font-weight: 600;
    color: var(--silver);
    white-space: nowrap;
    letter-spacing: 0.02em;
  }
  .card--front .brand { left: 20px; top: 52px; width: 220px; }
  .card--front .brand__dot { width: 56px; height: 56px; margin-bottom: 18px; }
  .card--front .brand__name { font-size: 14.5px; }

  .card--back .brand { left: 0; right: 0; top: 78px; }
  .card--back .brand__dot { width: 74px; height: 74px; margin-bottom: 24px; }
  .card--back .brand__name { font-size: 22px; }

  .contact {
    position: absolute;
    left: 284px;
    top: 86px;
    color: var(--text-light);
  }
  .contact__name {
    font-weight: 700;
    font-size: 16px;
    letter-spacing: 0.02em;
    text-transform: uppercase;
  }
  .contact__role {
    font-size: 11.5px;
    color: var(--text-muted);
    margin-top: 2px;
  }
  .contact__lines {
    margin-top: 20px;
    font-size: 11.5px;
    line-height: 17px;
    list-style: none;
  }
  .contact__label { color: var(--gold); font-weight: 700; }
  .contact__web-key { color: var(--gold); font-weight: 700; }

  .wave {
    position: absolute;
    left: 0;
    bottom: 0;
    width: 520px;
    height: 290px;
  }
</style>
</head>
<body>
  <section class="card card--front" aria-label="Business card front">
    <div class="brand">
      <span class="brand__dot"></span>
      <span class="brand__name">Harbourlight Gatherings Co.</span>
    </div>
    <div class="contact">
      <p class="contact__name">Darian Whitlock</p>
      <p class="contact__role">Event and Conference Specialist</p>
      <ul class="contact__lines">
        <li><span class="contact__label">M:</span> +61 (0) 491 238 604 · <span class="contact__label">T:</span> 1300 617 482</li>
        <li><span class="contact__label">E:</span> dariannw@lumorahostgroup.com.au</li>
        <li>www.<span class="contact__web-key">lumorahostgroup</span>.com.au</li>
      </ul>
    </div>
    <svg class="wave" viewBox="0 0 520 290" aria-hidden="true">
      <defs>
        <linearGradient id="goldBand" x1="0" y1="0" x2="1" y2="0">
          <stop offset="0" stop-color="#b8922f"/>
          <stop offset="0.35" stop-color="#f0d47c"/>
          <stop offset="0.7" stop-color="#c9a13d"/>
          <stop offset="1" stop-color="#a9832a"/>
        </linearGradient>
        <linearGradient id="shadeBand" x1="0" y1="0" x2="1" y2="0">
          <stop offset="0" stop-color="#1c1c1c"/>
          <stop offset="0.6" stop-color="#3a3a3a"/>
          <stop offset="1" stop-color="#262626"/>
        </linearGradient>
      </defs>
      <path d="M0,248 C140,214 300,198 380,208 C450,216 500,238 520,254 L520,290 L0,290 Z" fill="url(#goldBand)"/>
      <path d="M0,262 C140,228 300,212 380,220 C450,227 500,248 520,262 L520,290 L0,290 Z" fill="#f4f4f4"/>
      <path d="M0,268 C140,236 300,220 380,227 C450,234 500,255 520,269 L520,290 L0,290 Z" fill="url(#shadeBand)"/>
    </svg>
  </section>

  <section class="card card--back" aria-label="Business card back">
    <div class="brand">
      <span class="brand__dot"></span>
      <span class="brand__name">Harbourlight Gatherings Co.</span>
    </div>
  </section>
</body>
</html>
```